Game Box creation for Kids Classic Games for Outdoor Play

We need to design a game box (soft paper box or carton box) that will contain classic outdoor-old school kids games (teetotums, jumping ropes etc.). I am thinking the design to have a vintage feeling with a modern touch though.
If you come up with some thing different, its welcome..!
The box will have 7 compartments(dividers) inside each representing a game. The Box will have the following dimensions:
60cm(L)x30cm(W)x10cm(H).
Out of the 7 compartments, we need to have one long side divider (compartment) for a ball with its pump (20cm x 30 cm x 10cm) and 6 smaller compartments of 13cm x 15cm x 10cm.
We are thinking - but are not sure - if at the bottom of each compartment (game) there should be a painting/sketch showcasing the game.
We just thought we could call this project "The Wander Ledger" or "Crate of Whimsy" and include as well a small book which will explain how the games are played. Ideas are welcome on the booklet too.
**UPDATE: I have just found an EXCELLENT design that i want to follow. Please see attached and go with it.
Many many thanks!
Parents who will remember their youth and the games they played in the neighborhood, hence they will buy for their kids as a gift.
School

```html
<!DOCTYPE html>
<html lang="en">
<head>
<meta charset="utf-8">
<title>Crate of Whimsy – Box Design</title>
<link rel="stylesheet" href="https://fonts.googleapis.com/css2?family=Jost:wght@400;500&display=swap">
<style>
  :root {
    --backdrop: #e4e4e4;
    --kraft: #d8c6a3;
    --kraft-edge: #cdb993;
    --orange: #d8531c;
    --orange-deep: #c4461a;
    --ink: #1f1c1a;
  }
  * { box-sizing: border-box; margin: 0; padding: 0; }
  html, body {
    width: 1200px;
    height: 1000px;
    overflow: hidden;
    background: var(--backdrop);
    font-family: "Jost", "Futura", sans-serif;
    color: var(--ink);
  }
  .box-layout {
    position: absolute;
    left: 75px;
    top: 230px;
    display: flex;
    height: 540px;
  }
  .spine {
    width: 160px;
    height: 100%;
    background: var(--kraft);
    border-right: 1px solid var(--kraft-edge);
    display: flex;
    align-items: center;
    justify-content: center;
  }
  .spine-title {
    writing-mode: vertical-rl;
    transform: rotate(180deg);
    font-size: 58px;
    font-weight: 400;
    letter-spacing: 1px;
    white-space: nowrap;
  }
  .front {
    display: flex;
    height: 100%;
  }
  .front-intro {
    width: 350px;
    background: var(--kraft);
    padding: 110px 40px 0 70px;
  }
  .front-title {
    font-size: 66px;
    font-weight: 400;
    line-height: 1.02;
    letter-spacing: 0.5px;
  }
  .front-tagline {
    margin-top: 22px;
    font-size: 9px;
    line-height: 1.5;
    letter-spacing: 0.4px;
    text-transform: uppercase;
    max-width: 200px;
  }
  .game-panel {
    width: 540px;
    background: var(--orange);
    padding: 50px 40px 40px;
    display: grid;
    grid-template-columns: repeat(3, 1fr);
    grid-template-rows: repeat(2, 1fr);
    gap: 24px 30px;
  }
  .game-item {
    display: flex;
    flex-direction: column;
    align-items: center;
    gap: 12px;
  }
  .game-art {
    width: 100%;
    flex: 1;
    background: var(--orange-deep);
    border-radius: 6px;
  }
  .game-name {
    font-size: 10px;
    font-weight: 500;
    letter-spacing: 0.5px;
    text-transform: uppercase;
  }
</style>
</head>
<body>
  <main class="box-layout">
    <section class="spine">
      <h2 class="spine-title">CRATE OF WHIMSY</h2>
    </section>
    <section class="front">
      <div class="front-intro">
        <h1 class="front-title">CRATE OF<br>WHIMSY</h1>
        <p class="front-tagline">Lorem ipsum dolor sit amet, consectetur adipiscing elit, sed do eiusmod tempor</p>
      </div>
      <div class="game-panel">
        <figure class="game-item">
          <div class="game-art" role="img" aria-label="Line drawing of chalk sticks"></div>
          <figcaption class="game-name">Chalk</figcaption>
        </figure>
        <figure class="game-item">
          <div class="game-art" role="img" aria-label="Line drawing of a coiled jumping rope with wooden handles"></div>
          <figcaption class="game-name">Jumping Rope</figcaption>
        </figure>
        <figure class="game-item">
          <div class="game-art" role="img" aria-label="Line drawing of a looped Chinese rope"></div>
          <figcaption class="game-name">Chinese Rope</figcaption>
        </figure>
        <figure class="game-item">
          <div class="game-art" role="img" aria-label="Line drawing of five spoons arranged in a star"></div>
          <figcaption class="game-name">5 Spoons and 5 Eggs</figcaption>
        </figure>
        <figure class="game-item">
          <div class="game-art" role="img" aria-label="Line drawing of a wooden yo-yo with string"></div>
          <figcaption class="game-name">Wooden Yo Yo</figcaption>
        </figure>
        <figure class="game-item">
          <div class="game-art" role="img" aria-label="Line drawing of a stitched ball"></div>
          <figcaption class="game-name">Fun Ball</figcaption>
        </figure>
      </div>
    </section>
  </main>
</body>
</html>
```